Hopscotch Nell needs updated Marketing Material!

Moving business to a new location and am looking to update all marketing material, including business cards, postcards, flyers, website. I've attached a copy of my current business card.
Updates

Good Morning!  I just received my new business phone number.  It is 583-402-9176

Hello All Designers!

Thank you for all the submissions I have received so far!  I wanted to give you a bit more background on what Hopscotch Nell is all about:

I started this service when I was downsized out of a sales and marketing position.   A friend asked if I had time to run a few errands for her while she was at work.  "Lightbulb"!  I thought there must be more people that are over worked, over booked and want nothing more to do when they get home than spend time with their families or just relaxing.  And who wants to do all their running around on the weekends??  Hopscotch Nell was born!

I have been extremely fortunate with my business here in California.  However, this summer I will be moving to a small town in Pennsylvania and I will be in uncharted territory.  I hope to have marketing material that will "WOW" all new potential clients.  Letting them know that I offer a unique service that can put time back into their week and free up their weekends for more important things.

If there is anything else I can tell you in order to help you with your design process, please let me know!
Thank you!
Nellie

Target Market(s)

Busy working parents and young professionals with disposable income that would like to spend their down time doing things that they enjoy rather than doing errands.

Industry/Entity Type

Marketing

```html
<!DOCTYPE html>
<html lang="en">
<head>
<meta charset="utf-8">
<title>Hopscotch Nell – Business Card</title>
<link href="https://fonts.googleapis.com/css2?family=Quicksand:wght@400;500&display=swap" rel="stylesheet">
<style>
  :root {
    --page-bg: #5f6a6b;
    --band-yellow-top: #f4f51e;
    --band-yellow-bottom: #c9d10a;
    --blue-top: #1a34dc;
    --blue-bottom: #2222ee;
    --title-blue: #1f2fb8;
    --accent-yellow: #f2f23a;
    --card-white: #ffffff;
    --ink-grey: #3a3a3a;
  }
  * { margin: 0; padding: 0; box-sizing: border-box; }
  html, body {
    width: 1200px; height: 741px; overflow: hidden;
    background: var(--page-bg);
    font-family: "Quicksand", sans-serif;
  }
  .card {
    position: absolute;
    left: 400px;
    width: 408px;
    height: 236px;
    overflow: hidden;
  }
  /* Front */
  .card--front { top: 90px; background: linear-gradient(var(--blue-top), var(--blue-bottom)); }
  .brand-band {
    position: absolute; left: 0; top: 0; width: 100%; height: 83px;
    background: linear-gradient(var(--band-yellow-top), var(--band-yellow-bottom));
  }
  .brand-name {
    position: absolute; left: 161px; top: 19px;
    font-size: 31px; font-weight: 400; color: var(--title-blue); line-height: 1;
    white-space: nowrap;
  }
  .brand-tagline {
    position: absolute; left: 162px; top: 56px;
    font-size: 11.5px; font-weight: 500; color: var(--title-blue);
    white-space: nowrap;
  }
  .owner { position: absolute; left: 17px; top: 122px; color: var(--accent-yellow); }
  .owner-name { font-size: 16px; font-weight: 400; margin-bottom: 10px; }
  .contact { display: flex; align-items: center; gap: 5px; font-size: 8.5px; font-weight: 500; margin-bottom: 4px; }
  .contact svg { width: 8px; height: 8px; flex: none; }
  .services {
    position: absolute; left: 162px; top: 122px; list-style: none;
    color: var(--accent-yellow); font-size: 10px; font-weight: 500;
  }
  .services li { height: 18px; line-height: 18px; white-space: nowrap; }
  /* Back */
  .card--back { top: 413px; background: var(--card-white); }
  .back-mark {
    position: absolute; left: 0; top: 52px; width: 100%;
    display: flex; justify-content: center; align-items: center; gap: 10px;
    font-size: 26px; font-weight: 500; color: var(--title-blue);
  }
  .back-mark .dot { width: 18px; height: 18px; border-radius: 50%; background: var(--title-blue); }
  .slogan {
    position: absolute; left: 0; top: 130px; width: 100%; text-align: center;
    font-size: 20px; font-weight: 400; color: var(--ink-grey);
    letter-spacing: 1px; word-spacing: 4px; white-space: nowrap;
  }
</style>
</head>
<body>
  <section class="card card--front">
    <div class="brand-band">
      <h1 class="brand-name">Hopscotch Nell</h1>
      <p class="brand-tagline">Personal Concierge and Errand Service</p>
    </div>
    <div class="owner">
      <p class="owner-name">Nellie Calder</p>
      <p class="contact">
        <svg viewBox="0 0 8 8"><rect x="2" y="0.5" width="4" height="7" rx="0.8" fill="none" stroke="currentColor" stroke-width="0.8"/></svg>
        583.402.9176
      </p>
      <p class="contact">
        <svg viewBox="0 0 8 8"><rect x="0.5" y="1.5" width="7" height="5" fill="none" stroke="currentColor" stroke-width="0.8"/><path d="M0.5 1.5 L4 4.5 L7.5 1.5" fill="none" stroke="currentColor" stroke-width="0.8"/></svg>
        nellie@hopscotchnell.biz
      </p>
    </div>
    <ul class="services">
      <li>Personal shopping and Errands</li>
      <li>Household management</li>
      <li>Corporate concierge</li>
      <li>Project management</li>
      <li>Group rates for Teachers and seniors</li>
    </ul>
  </section>

  <section class="card card--back">
    <div class="back-mark"><span class="dot"></span>Hopscotch Nell</div>
    <p class="slogan">We hop around so you don't have to!</p>
  </section>
</body>
</html>
```